Corvid Aviation - Learn to Fly

Our customers are people who span all ages and genders that are interested in learning how to fly airplanes for fun or as a career, or who would like to advance their piloting skills.

Flight training we offer:
Private Pilot Certificate
Instrument Rating
Commercial Pilot Certificate
Sport Pilot Certificate: Powered Parachute
Drone Pilot Training

Ground School we offer:
Sport Pilot Ground School
Private Pilot Ground School
Instrument Pilot Ground School
Drone Pilot Ground School

Target Market(s)

Bessemer, Alabama, United States: High school students, college students, career changers. Someone interested in learning to fly for fun or for a career in the United States.

Industry/Entity Type

Aviation

Requirements
Must have
• I would like for you to enjoy some creative freedom here. The feeling and image we want to portray is a professional, but also very exciting and energizing image. The prospective customer and student should see the brochure and be excited to call us or come out for more information on learning how to fly. Our tag line is: "Small Step Today, Giant Leap Tomorrow."
Nice to have
• It would be helpful if you can do some reading or a little research on each of the types of training that we offer so that you will understand what should be included in the brochure. Our goal is to let everyone know who we are, what we offer, and how to contact us.

This may help some with design ideas: The name Corvid Aviation is inspired by the Orbix Skyward space program because the owner of the flight school is a big fan of Orbix and the Skyward mission.

```html
<!DOCTYPE html>
<html lang="en">
<head>
<meta charset="utf-8">
<title>Corvid Aviation – Brochure Cover</title>
<link href="https://fonts.googleapis.com/css2?family=Montserrat:wght@300;400;600;700&display=swap" rel="stylesheet">
<style>
  :root{
    --navy:#1a2234;
    --navy-light:#28364c;
    --red:#c1272d;
    --white:#ffffff;
    --ink:#2a2f3a;
    --muted:#c9cfdb;
    --stage:#6e6e6e;
  }
  *{margin:0;padding:0;box-sizing:border-box}
  html,body{width:1200px;height:789px;overflow:hidden;background:var(--stage)}
  body{font-family:"Montserrat",sans-serif;display:flex}
  .page{position:relative;width:600px;height:789px;overflow:hidden}
  .page svg.bg{position:absolute;inset:0}
  .abs{position:absolute}

  /* back cover */
  .section-title{font-weight:300;font-size:40px;color:var(--ink);letter-spacing:.5px}
  .section-title strong{font-weight:700;color:var(--red)}
  .about-title{left:70px;top:92px}
  .rule{height:1px;background:var(--ink);opacity:.6}
  .about-rule{left:70px;top:146px;width:300px}
  .about-copy{left:70px;top:166px;width:320px;font-size:11px;line-height:16px;color:var(--ink)}
  .about-copy p+p{margin-top:14px}
  .cta{left:70px;top:392px;font-size:25px;line-height:36px;font-weight:300;color:var(--ink)}
  .cta b{font-weight:700;color:var(--red)}
  .contact-title{left:70px;top:606px;color:var(--white)}
  .contact-rule{left:70px;top:660px;width:300px;background:var(--muted)}
  .contact-list{left:70px;top:676px;list-style:none;font-size:11px;font-weight:300;color:var(--muted)}
  .contact-list li{display:flex;gap:10px;align-items:flex-start;margin-bottom:9px;line-height:15px}
  .contact-list svg{flex:none;margin-top:1px}
  .social{left:430px;top:712px;display:flex;gap:10px}
  .social span{width:22px;height:22px;border:1.5px solid var(--muted);border-radius:50%}

  .brand-mark{display:flex;align-items:center;justify-content:center;border-radius:50%;background:var(--white);border:4px solid var(--red);text-align:center;font-weight:700;color:var(--navy);text-transform:uppercase;letter-spacing:1px}
  .brand-small{left:410px;top:510px;width:104px;height:104px;font-size:12px;line-height:16px}
  .brand-large{left:246px;top:340px;width:150px;height:150px;font-size:17px;line-height:22px}

  /* front cover */
  .tagline{left:0;width:600px;top:530px;text-align:center;color:var(--white);text-transform:uppercase}
  .tagline .light{display:block;font-weight:300;font-size:24px;letter-spacing:1px}
  .tagline .bold{display:block;font-weight:700;font-size:28px;letter-spacing:1px;margin-top:4px}
  .front-rule{left:170px;top:622px;width:260px;background:var(--muted)}
  .front-url{left:0;width:600px;top:640px;text-align:center;font-size:12px;font-weight:300;letter-spacing:2px;color:var(--muted)}
</style>
</head>
<body>

<section class="page back-cover">
  <svg class="bg" width="600" height="789" viewBox="0 0 600 789">
    <defs>
      <linearGradient id="teamPhoto" x1="0" y1="0" x2="1" y2="1">
        <stop offset="0" stop-color="#e6e9f0"/>
        <stop offset="1" stop-color="#c4cad7"/>
      </linearGradient>
    </defs>
    <rect width="600" height="789" fill="var(--navy)"/>
    <path role="img" aria-label="Faded photo of a flight instructor and student reviewing a tablet in a hangar" d="M0,0 H600 V330 Q330,520 0,560 Z" fill="url(#teamPhoto)"/>
    <path d="M0,560 Q330,520 600,330" fill="none" stroke="var(--red)" stroke-width="5"/>
  </svg>

  <h2 class="abs section-title about-title">About <strong>Us</strong></h2>
  <div class="abs rule about-rule"></div>
  <div class="abs about-copy">
    <p>Lorem ipsum dolor sit amet, consectetur adipiscing elit, sed do eiusmod tempor incididunt ut labore et dolore magna aliqua. Ut enim ad minim veniam, quis nostrud exercitation ullamco laboris nisi ut aliquip ex ea commodo consequat. Duis aute irure dolor in reprehenderit in voluptate velit esse cillum dolore eu fugiat nulla pariatur. Excepteur sint occaecat cupidatat non proident, sunt in culpa qui officia deserunt mollit anim id est laborum.</p>
    <p>Lorem ipsum dolor sit amet, consectetur adipiscing elit, sed do eiusmod tempor incididunt ut labore et dolore magna aliqua. Ut enim ad minim veniam.</p>
  </div>
  <p class="abs cta"><b>call us</b> for more information<br>on <b>learning how to fly.</b></p>

  <div class="abs brand-mark brand-small">Corvid<br>Aviation</div>

  <h2 class="abs section-title contact-title">Contact <strong>Us</strong></h2>
  <div class="abs rule contact-rule"></div>
  <ul class="abs contact-list">
    <li><svg width="10" height="12" viewBox="0 0 10 12"><path d="M5 11 C2 7 1 5.5 1 4 a4 4 0 0 1 8 0 c0 1.5-1 3-4 7z" fill="none" stroke="currentColor"/><circle cx="5" cy="4" r="1.3" fill="currentColor"/></svg><span>Address Line_1, Address Line_1<br>Address Line_2</span></li>
    <li><svg width="10" height="12" viewBox="0 0 12 12"><path d="M3 1 L5 4 L4 5 Q5 7.5 7 8 L8 7 L11 9 L10 11 Q4 11 1 3 Z" fill="none" stroke="currentColor"/></svg><span>+0123 456 789</span></li>
    <li><svg width="10" height="12" viewBox="0 0 12 12"><rect x="1" y="3" width="10" height="7" fill="none" stroke="currentColor"/><path d="M1 3 L6 7 L11 3" fill="none" stroke="currentColor"/></svg><span>info@corvidaviation.com</span></li>
    <li><svg width="10" height="12" viewBox="0 0 12 12"><circle cx="6" cy="6" r="5" fill="none" stroke="currentColor"/><path d="M1 6 H11 M6 1 Q3 6 6 11 Q9 6 6 1" fill="none" stroke="currentColor"/></svg><span>www.corvidaviation.com</span></li>
  </ul>
  <div class="abs social" aria-label="Social links"><span></span><span></span><span></span><span></span></div>
</section>

<section class="page front-cover">
  <svg class="bg" width="600" height="789" viewBox="0 0 600 789">
    <defs>
      <linearGradient id="fieldPhoto" x1="0" y1="0" x2="0" y2="1">
        <stop offset="0" stop-color="#ecebef"/>
        <stop offset=".38" stop-color="#cfc6b8"/>
        <stop offset=".55" stop-color="#a9834a"/>
        <stop offset="1" stop-color="#7e5a26"/>
      </linearGradient>
      <linearGradient id="frontNavy" x1="0" y1="0" x2="1" y2="0">
        <stop offset="0" stop-color="var(--navy-light)"/>
        <stop offset="1" stop-color="var(--navy)"/>
      </linearGradient>
    </defs>
    <rect width="600" height="789" fill="url(#frontNavy)"/>
    <path role="img" aria-label="Photo of a child in an aviator cap holding up a wooden toy biplane in a golden meadow" d="M0,0 H600 V250 Q480,400 320,420 Q180,440 0,330 Z" fill="url(#fieldPhoto)"/>
    <path d="M0,330 Q180,440 320,420 Q480,400 600,250" fill="none" stroke="var(--red)" stroke-width="5"/>
  </svg>

  <div class="abs brand-mark brand-large">Corvid<br>Aviation</div>

  <h1 class="abs tagline"><span class="light">Small Step Today</span><span class="bold">Giant Leap Tomorrow</span></h1>
  <div class="abs rule front-rule"></div>
  <p class="abs front-url">www.corvidaviation.com</p>
</section>

</body>
</html>
```